Building Company Business Card Design

I am looking to get a business card designed for my Building Company. Please find the logo attached.

Industry/Entity Type

Business

Contact Information for Business Card

Mobile 0472 913 046
Email admin@tarrowconstructworks.com.au
Website www.tarrowconstructworks.com.au

Colors
0255a3

```html
<!DOCTYPE html>
<html lang="en">
<head>
<meta charset="UTF-8">
<title>Tarrow Construct Works – Business Card</title>
<link rel="stylesheet" href="https://fonts.googleapis.com/css2?family=Roboto:wght@400;500&family=Roboto+Condensed:wght@700&display=swap">
<style>
  :root {
    --brand-blue: #0255a3;
    --card-white: #f5f5f5;
    --text-grey: #555759;
    --title-grey: #6b6d70;
    --stage: #e6e3df;
    --on-blue: #ffffff;
  }
  * { margin: 0; padding: 0; box-sizing: border-box; }
  html, body { width: 1200px; height: 960px; overflow: hidden; }
  body {
    background: var(--stage);
    position: relative;
    font-family: "Roboto", Arial, sans-serif;
  }
  .card {
    position: absolute;
    width: 600px;
    height: 343px;
  }
  .card--front {
    left: 314px; top: 113px;
    background: var(--card-white);
    text-align: center;
  }
  .card--back {
    left: 312px; top: 472px;
    background: var(--brand-blue);
    text-align: center;
  }
  .wordmark {
    position: absolute;
    left: 0; right: 0;
    font-weight: 500;
    letter-spacing: 1px;
  }
  .card--front .wordmark {
    top: 84px;
    font-size: 34px;
    color: var(--brand-blue);
  }
  .card--back .wordmark {
    top: 138px;
    font-size: 30px;
    color: var(--on-blue);
  }
  .holder-name {
    position: absolute;
    top: 207px; left: 0; right: 0;
    font-family: "Roboto Condensed", Arial, sans-serif;
    font-weight: 700;
    font-size: 24px;
    color: var(--brand-blue);
  }
  .holder-title {
    position: absolute;
    top: 235px; left: 0; right: 0;
    font-size: 15px;
    color: var(--title-grey);
  }
  .contact {
    position: absolute;
    top: 270px; left: 0; right: 0;
    font-size: 14.5px;
    line-height: 19px;
    color: var(--text-grey);
  }
  .contact .label { color: var(--brand-blue); font-weight: 500; }
  .website {
    position: absolute;
    top: 288px; left: 0; right: 0;
    font-size: 15px;
    letter-spacing: 3px;
    color: var(--on-blue);
  }
</style>
</head>
<body>
  <section class="card card--front">
    <div class="wordmark">TARROW CONSTRUCT WORKS</div>
    <div class="holder-name">DANIEL HARKER</div>
    <div class="holder-title">CEO/FOUNDER</div>
    <div class="contact">
      <div>214 Wattle Street, Parramatta NSW 2150 | <span class="label">P:</span> 0472 913 046</div>
      <div><span class="label">E:</span> admin@tarrowconstructworks.com.au <span class="label">W:</span> tarrowconstructworks.com.au</div>
    </div>
  </section>

  <section class="card card--back">
    <div class="wordmark">TARROW CONSTRUCT WORKS</div>
    <div class="website">www.tarrowconstructworks.com.au</div>
  </section>
</body>
</html>
```